A land page lead collector for people who want to reduce there postage costs

We are looking to create a single page website landing page to collect leads of people who want to reduce there postage costs.

The form should basically ask:

Name:
Business Name:
Address:
Town:
Post Code:
Email:
Phone:
Letter Volume Per Week:
Parcel Volume Per Week:

We should basically be advertising cheaper postage costs.

We will not be showing prices on this website we will just be collecting the leads.

Our competition website is as follows https://mailfernquest.com

But we are not a online service. This is just a collector to get leads of people who want to save money on there postage costs.
Updates

Target Market(s)

Small and medium sized enterprises

Industry/Entity Type

Advertising

Number of Pages Required

1 page

Colors
ec2027
0356a4

Requirements
Must have
• Form above the fold of the page
Nice to have
• Colour red and blue.
• Parallax design would be nice.

```html
<!DOCTYPE html>
<html lang="en">
<head>
<meta charset="utf-8">
<title>Stampwell – Postage Cost Reduction</title>
<link href="https://fonts.googleapis.com/css2?family=Arimo:wght@400;700&family=PT+Sans:wght@700&display=swap" rel="stylesheet">
<style>
:root{
  --red:#ec2027;
  --blue:#0356a4;
  --ink:#333;
  --muted:#777;
  --field:#f3f3f3;
  --line:#dcdcdc;
  --panel:#f7f7f7;
  --footer:#3a3a3a;
}
*{margin:0;padding:0;box-sizing:border-box}
html,body{width:1003px;height:1200px;overflow:hidden;background:#fff;font-family:"Arimo",Arial,sans-serif;color:var(--ink)}
.page{position:relative;width:1003px;height:1200px;border-top:3px solid var(--red)}
.abs{position:absolute}
.logo{left:82px;top:36px;font-size:24px;color:var(--blue);letter-spacing:-0.3px}
.nav{right:81px;top:42px;display:flex;gap:42px;font-size:10.5px;list-style:none}
.nav li{color:#444}
.nav li.active{color:var(--red)}
.hero{left:82px;top:90px;width:840px;height:392px;background:linear-gradient(100deg,#6f7f5a 0%,#8a9276 30%,#9aa0a0 55%,#7e8f6a 75%,#c9d1a8 100%)}
.slider-arrows{left:862px;top:446px;display:flex;gap:1px}
.slider-arrows span{width:19px;height:19px;background:#d63a26;display:flex;align-items:center;justify-content:center}
.lead-card{left:110px;top:174px;width:276px;height:345px;background:#fff;border:1px solid #ddd;border-radius:6px;box-shadow:0 6px 6px -4px rgba(0,0,0,.25)}
.ribbon{left:146px;top:152px;width:218px;height:60px}
.ribbon-text{left:146px;top:158px;width:218px;text-align:center;font-family:"PT Sans",sans-serif;font-weight:700;font-size:13px;line-height:18px;color:#fff}
.field{position:absolute;height:28px;background:var(--field);border:1px solid var(--line);font-size:9.5px;color:#666;padding:0 9px;display:flex;align-items:center}
.subscribe{left:189px;top:476px;width:120px;height:31px;background:linear-gradient(#1f6fc0,#0a4e96);color:#fff;font-weight:700;font-size:12px;display:flex;align-items:center;justify-content:center;border-radius:2px}
.welcome{left:0;width:1003px;top:528px;text-align:center;font-size:20px;color:var(--blue)}
.welcome em{font-style:normal;color:var(--red)}
.intro{left:180px;width:643px;top:564px;text-align:center;font-size:8.6px;line-height:16.5px;color:#666}
.feature{width:240px;text-align:center}
.feature .thumb{width:94px;height:94px;border-radius:50%;margin:0 auto;border:5px solid #e9e9e9}
.feature h3{font-weight:400;font-size:12px;margin-top:18px;color:#333}
.feature p{font-size:8.6px;line-height:16.5px;color:#777;margin-top:9px}
.panel{left:82px;top:843px;width:840px;height:266px;background:var(--panel);border:2px solid #ececec}
.stamp{left:104px;top:867px;width:264px;height:222px;background:#111;padding:6px}
.stamp-in{width:100%;height:100%;background:#fff;padding:8px}
.stamp-photo{width:100%;height:100%;background:linear-gradient(180deg,#7fb2e0 0%,#a9c9e4 28%,#c9a44c 55%,#9a7428 85%,#6d5a35 100%)}
.panel-title{left:407px;top:870px;font-size:14px;color:var(--red)}
.panel-text{left:407px;top:899px;width:496px;font-size:8.6px;line-height:17px;color:#888}
.checks{left:407px;top:963px;list-style:none}
.checks li{display:flex;align-items:center;gap:12px;font-size:8.6px;color:#555;height:23.6px}
.footer{left:0;top:1125px;width:1003px;height:75px;background:var(--footer)}
.copy{left:83px;top:1159px;font-size:8.6px;color:#ccc}
.social{right:83px;top:1152px;display:flex;gap:7px}
.social span{width:25px;height:25px;border:1.5px solid #999;border-radius:50%}
</style>
</head>
<body>
<div class="page">
  <div class="abs logo">STAMPWELL</div>
  <ul class="abs nav">
    <li class="active">HOME</li><li>ABOUT US</li><li>SERVICES</li><li>NEWS</li><li>TESTIMONIALS</li><li>CONTACT US</li>
  </ul>

  <div class="abs hero" role="img" aria-label="Child posting a letter into a red post box on a leafy street"></div>
  <div class="abs slider-arrows">
    <span><svg width="8" height="10" viewBox="0 0 8 10"><path d="M6 1 2 5l4 4" fill="none" stroke="#fff" stroke-width="1.4"/></svg></span>
    <span><svg width="8" height="10" viewBox="0 0 8 10"><path d="M2 1l4 4-4 4" fill="none" stroke="#fff" stroke-width="1.4"/></svg></span>
  </div>

  <div class="abs lead-card"></div>
  <svg class="abs ribbon" viewBox="0 0 218 60">
    <defs><linearGradient id="rib" x1="0" y1="0" x2="0" y2="1"><stop offset="0" stop-color="#2f7fd0"/><stop offset="1" stop-color="#0a4b94"/></linearGradient></defs>
    <path d="M0 24 12 4h14z" fill="#0a3f7c"/>
    <path d="M218 24 206 4h-14z" fill="#0a3f7c"/>
    <path d="M20 2h178l-18 44q-6 12-20 12H58q-14 0-20-12z" fill="#c9ced6"/>
    <path d="M24 0h170l-17 42q-5 11-18 11H59q-13 0-18-11z" fill="url(#rib)"/>
  </svg>
  <div class="abs ribbon-text">POSTAGE COST<br>REDUCTION</div>

  <div class="field" style="left:134px;top:225px;width:227px">Name :</div>
  <div class="field" style="left:134px;top:261px;width:227px">Business Name :</div>
  <div class="field" style="left:134px;top:295px;width:227px">Address :</div>
  <div class="field" style="left:134px;top:330px;width:109px">Town :</div>
  <div class="field" style="left:252px;top:330px;width:109px">Post Code :</div>
  <div class="field" style="left:134px;top:366px;width:227px">Email :</div>
  <div class="field" style="left:134px;top:400px;width:227px">Letter Volume Per Week :</div>
  <div class="field" style="left:134px;top:435px;width:227px">Parcel Volume Per Week :</div>
  <div class="abs subscribe">SUBSCRIBE</div>

  <h1 class="abs welcome" style="font-weight:400"><em>WELCOME TO</em> OUR SITE</h1>
  <p class="abs intro">It is a long established fact that a reader will be distracted by the readable content of a page when looking at its layout. The point of using Lorem Ipsum is that it has a more-or-less normal distribution of letters, as opposed to using 'Content here, content here', making it look like readable English.</p>

  <div class="abs feature" style="left:93px;top:617px">
    <div class="thumb" role="img" aria-label="Child at a red post box" style="background:linear-gradient(90deg,#b3201c,#6a3a2a)"></div>
    <h3>POSTAGE COST</h3>
    <p>It is a long established fact that a reader will be distracted by the readable content of a page when looking at its layout- making it look like readable English.</p>
  </div>
  <div class="abs feature" style="left:374px;top:617px">
    <div class="thumb" role="img" aria-label="Castle on a postage stamp" style="background:linear-gradient(180deg,#8fb8e0,#c9a44c 60%,#7a5e2a)"></div>
    <h3>REDUCE POSTAGE</h3>
    <p>It is a long established fact that a reader will be distracted by the readable content of a page when looking at its layout- making it look like readable English.</p>
  </div>
  <div class="abs feature" style="left:668px;top:617px">
    <div class="thumb" role="img" aria-label="Child posting a letter" style="background:linear-gradient(90deg,#c8c0b8,#d42a2a)"></div>
    <h3>POSTAGE COST</h3>
    <p>It is a long established fact that a reader will be distracted by the readable content of a page when looking at its layout- making it look like readable English.</p>
  </div>

  <div class="abs panel"></div>
  <div class="abs stamp"><div class="stamp-in"><div class="stamp-photo" role="img" aria-label="First class postage stamp showing a castle"></div></div></div>
  <h2 class="abs panel-title" style="font-weight:400">NEQUE PORRO QUISQUAM EST QUI DOLOREM IPSUM</h2>
  <p class="abs panel-text">To keep a check on your costs even further, Parcelora also offers an end-to-end service on the complete mailing – not just the postage. Effectively, we will act as your mailroom: we'll print your mail on high quality digital printers, stuff the envelopes mechani-cally and add the postage while we are sorting the post. This process saves businesses even more money.</p>
  <ul class="abs checks">
    <li><svg width="11" height="10" viewBox="0 0 11 10"><rect x="0.7" y="1.7" width="7.6" height="7.6" fill="none" stroke="#0356a4" stroke-width="1.4"/><path d="M2.5 5 4.5 7 10 1" fill="none" stroke="#0356a4" stroke-width="1.8"/></svg>Comprehensive mail sorting facilities</li>
    <li><svg width="11" height="10" viewBox="0 0 11 10"><rect x="0.7" y="1.7" width="7.6" height="7.6" fill="none" stroke="#0356a4" stroke-width="1.4"/><path d="M2.5 5 4.5 7 10 1" fill="none" stroke="#0356a4" stroke-width="1.8"/></svg>Checklist Tick &nbsp;access to DSAs, including National Post</li>
    <li><svg width="11" height="10" viewBox="0 0 11 10"><rect x="0.7" y="1.7" width="7.6" height="7.6" fill="none" stroke="#0356a4" stroke-width="1.4"/><path d="M2.5 5 4.5 7 10 1" fill="none" stroke="#0356a4" stroke-width="1.8"/></svg>Checklist Tick &nbsp;the capacity to process huge volumes of mail daily</li>
    <li><svg width="11" height="10" viewBox="0 0 11 10"><rect x="0.7" y="1.7" width="7.6" height="7.6" fill="none" stroke="#0356a4" stroke-width="1.4"/><path d="M2.5 5 4.5 7 10 1" fill="none" stroke="#0356a4" stroke-width="1.8"/></svg>Checklist Tick &nbsp;handling of various mail items, not just letters</li>
    <li><svg width="11" height="10" viewBox="0 0 11 10"><rect x="0.7" y="1.7" width="7.6" height="7.6" fill="none" stroke="#0356a4" stroke-width="1.4"/><path d="M2.5 5 4.5 7 10 1" fill="none" stroke="#0356a4" stroke-width="1.8"/></svg>Checklist Tick &nbsp;access to international mailing networks as well as UK ones.</li>
  </ul>

  <div class="abs footer"></div>
  <div class="abs copy">© Copyright 2014 Stampwell. All Right Reserved.</div>
  <div class="abs social"><span></span><span></span><span></span><span></span><span></span></div>
</div>
</body>
</html>
```